Retractable Banner Design - Bluepine Networking Event

Bluepine Financial Services, Inc.
Quarterly Networking Event

Hosted by Darnell Okafor & Marcus Dunleavy

"Home of the Mortgage Originating Real Estate Experts, who earn MORE on Every Buyers Transaction" - Curtis Pemberton

1) Make "MORE" and first letters spelling "MORE" stand out"
2) Add picture of Curtis Pemberton to quote.
3) Make Quote in Italics

For more information
follow us @goreachbluepine on FB & IG (use FB & IG logo instead)
or Call (800) 555-0142
NMLS #318760

```html
<!DOCTYPE html>
<html lang="en">
<head>
<meta charset="utf-8">
<title>Bluepine Quarterly Networking Event Banner</title>
<link href="https://fonts.googleapis.com/css2?family=Merriweather:ital,wght@0,400;0,700;0,900;1,700;1,900&display=swap" rel="stylesheet">
<style>
  :root {
    --backdrop: #a9a9a9;
    --white: #ffffff;
    --navy: #27327e;
    --gold: #d6a42c;
    --sky: #1f8fd0;
    --ink: #050505;
    --photo-top: #d9a766;
    --photo-bottom: #3a3f4c;
    --portrait: #8a6a55;
  }
  * { box-sizing: border-box; margin: 0; padding: 0; }
  html, body { width: 1200px; height: 1117px; overflow: hidden; }
  body {
    background: var(--backdrop);
    font-family: "Merriweather", Georgia, serif;
    position: relative;
  }
  .banner {
    position: absolute;
    left: 380px; top: 25px;
    width: 440px; height: 1067px;
    background: var(--white);
    overflow: hidden;
  }
  .banner-shapes { position: absolute; inset: 0; }
  .brand {
    position: absolute; top: 42px; left: 0; width: 100%;
    text-align: center; color: var(--navy);
  }
  .brand-name {
    display: inline-flex; align-items: center; gap: 8px;
    font-weight: 900; font-size: 21px; letter-spacing: 0.5px;
  }
  .brand-mark {
    width: 16px; height: 16px; border-radius: 50%;
    background: var(--gold); display: inline-block;
  }
  .brand-tagline { font-size: 7.5px; font-weight: 700; margin-top: 6px; letter-spacing: 0.2px; }
  .brand-est { font-size: 8px; font-weight: 700; margin-top: 4px; letter-spacing: 2px; color: #555; }
  .hosts-photo {
    position: absolute; left: 0; top: 300px; width: 440px; height: 345px;
    background: linear-gradient(180deg, var(--photo-top) 0%, #8f8a86 45%, var(--photo-bottom) 100%);
  }
  .event-title {
    position: absolute; top: 204px; left: 0; width: 100%;
    text-align: center; line-height: 1.05; font-weight: 700;
  }
  .event-title .line-quarterly { color: var(--white); font-size: 46px; display: block; }
  .event-title .line-networking { color: var(--gold); font-size: 52px; display: block; }
  .event-title .line-event { color: var(--white); font-size: 40px; display: block; }
  .host-label {
    position: absolute; top: 610px; left: 50%; transform: translateX(-50%);
    background: var(--sky); color: var(--white);
    font-weight: 700; font-size: 15px; padding: 2px 12px 4px;
    border-radius: 8px 8px 0 0; z-index: 2; white-space: nowrap;
  }
  .host-badge {
    position: absolute; top: 625px; left: 50%; transform: translateX(-50%);
    width: 344px; height: 46px;
    background: var(--navy); border: 2px solid var(--white);
    border-radius: 6px; box-shadow: 0 2px 4px rgba(0,0,0,0.25);
    display: flex; align-items: center; justify-content: center;
    font-weight: 700; font-size: 14.5px; color: var(--white); padding-top: 6px;
  }
  .host-badge .first { color: var(--gold); }
  .quote {
    position: absolute; top: 684px; left: 0; width: 100%;
    text-align: center; color: var(--navy);
    font-weight: 700; font-style: italic; font-size: 23px; line-height: 1.2;
  }
  .quote .acrostic { color: var(--gold); font-weight: 900; }
  .quote .accent-more { color: var(--gold); font-weight: 900; }
  .quote .accent-buyers { color: var(--sky); }
  .quote-credit {
    position: absolute; top: 830px; left: 0; width: 100%;
    display: flex; align-items: center; justify-content: center; gap: 10px;
    color: var(--navy); font-weight: 700; font-size: 14px;
  }
  .credit-portrait {
    width: 44px; height: 44px; border-radius: 50%;
    background: radial-gradient(circle at 50% 40%, #b48a6c 0%, var(--portrait) 60%, #3d3440 100%);
    border: 2px solid var(--gold);
  }
  .contact {
    position: absolute; top: 950px; left: 0; width: 100%;
    text-align: center; color: var(--white);
    font-weight: 700; font-size: 16px; line-height: 1.3;
  }
  .network-dot {
    display: inline-block; width: 13px; height: 13px; border-radius: 50%;
    background: var(--gold); vertical-align: middle; margin-left: 3px;
  }
  .contact .license { color: var(--sky); font-size: 10px; font-weight: 400; margin-top: 4px; }
</style>
</head>
<body>
  <div class="banner">
    <div class="hosts-photo" role="img" aria-label="Photo of the two event hosts smiling in front of a city skyline at sunset"></div>

    <svg class="banner-shapes" width="440" height="1067" viewBox="0 0 440 1067" aria-hidden="true">
      <path d="M0 140 Q220 210 440 128 L440 155 Q220 225 0 165 Z" fill="var(--gold)"/>
      <path d="M0 160 Q220 222 440 150 L440 160 Q220 232 0 170 Z" fill="var(--sky)"/>
      <path d="M0 168 Q220 232 440 158 L440 349 Q220 430 0 349 Z" fill="var(--navy)"/>
      <path d="M0 630 Q220 660 440 640 L440 1067 L0 1067 Z" fill="var(--white)"/>
      <path d="M0 921 Q220 860 440 942 L440 1067 L0 1067 Z" fill="var(--sky)"/>
      <path d="M0 929 Q220 870 440 950 L440 1067 L0 1067 Z" fill="var(--white)"/>
      <path d="M0 934 Q220 876 440 955 L440 1067 L0 1067 Z" fill="var(--gold)"/>
      <path d="M0 956 Q220 905 440 972 L440 1067 L0 1067 Z" fill="var(--ink)"/>
    </svg>

    <header class="brand">
      <div class="brand-name"><span class="brand-mark"></span>BLUEPINE FINANCIAL SERVICES</div>
      <div class="brand-tagline">YOU REACH BLUEPINE, WE'LL HANDLE THE REST.</div>
      <div class="brand-est">EST. 1997</div>
    </header>

    <h1 class="event-title">
      <span class="line-quarterly">Quarterly</span>
      <span class="line-networking">Networking</span>
      <span class="line-event">Event</span>
    </h1>

    <div class="host-label">Hosted by</div>
    <div class="host-badge">
      <span><span class="first">Darnell</span> Okafor &amp; <span class="first">Marcus</span> Dunleavy</span>
    </div>

    <blockquote class="quote">
      “Home of the<br>
      <span class="acrostic">M</span>ortgage <span class="acrostic">O</span>riginating<br>
      <span class="acrostic">R</span>eal <span class="acrostic">E</span>state Experts,<br>
      who earn <span class="accent-more">MORE</span> on Every<br>
      <span class="accent-buyers">Buyers Transaction</span>”
    </blockquote>

    <div class="quote-credit">
      <div class="credit-portrait" role="img" aria-label="Portrait photo of Curtis Pemberton"></div>
      <span>— Curtis Pemberton</span>
    </div>

    <footer class="contact">
      For more information<br>
      follow us @goreachbluepine on <span class="network-dot"></span><span class="network-dot"></span><br>
      or Call (800) 555-0142
      <div class="license">NMLS #318760</div>
    </footer>
  </div>
</body>
</html>
```